Business Card Design For Tidecrest Audio

Tidecrest Audio is a small pro-audio company providing rental and install services for professional sound reinforcement. Focus is gigs (any gigs) needing high quality audio; from corporate to chamber music to hard hitting rock.

Tidecrest Audio
Pro-audio for your gig ... goosebump good
Doran Pelley
doran@tidecrestaudio.example.com.au
0482 356 071

We need a business card design and an "drop-off"' larger card (eg. one third A4 size: 99mm wide x 210mm high) with more details.
Updates

Please note I've had limited internet access for last few days and for the next four.  The work so far looks great .. I'll provide some individual feedback on the designs now.  Great work, many thanks, love the creativity!

Doran

Industry/Entity Type

Business

```html
<!DOCTYPE html>
<html lang="en">
<head>
<meta charset="utf-8">
<title>Tidecrest Audio – Business Card and Drop-off Card</title>
<link rel="stylesheet" href="https://fonts.googleapis.com/css2?family=Comfortaa:wght@300;400;700&display=swap">
<style>
  :root {
    --stage: #000000;
    --silver-light: #e4e4e4;
    --silver-mid: #cfcfcf;
    --silver-dark: #b4b4b4;
    --glow: rgba(255, 255, 255, 0.55);
    --brand-orange: #e8901a;
    --name-cyan: #00f0ff;
    --rule-orange: #f0a040;
    --rule-soft: rgba(150, 150, 150, 0.7);
  }
  * { box-sizing: border-box; margin: 0; padding: 0; }
  html, body {
    width: 1200px; height: 1000px; overflow: hidden;
    background: var(--stage);
    font-family: "Comfortaa", sans-serif;
  }
  .canvas { position: relative; width: 1200px; height: 1000px; }

  .card {
    position: absolute;
    border-radius: 5px;
    background: radial-gradient(ellipse at 70% 75%, var(--silver-light) 0%, var(--silver-mid) 45%, var(--silver-dark) 100%);
    box-shadow: 0 0 14px 4px var(--glow);
    text-align: center;
  }
  .card--business { left: 135px; top: 398px; width: 358px; height: 204px; }
  .card--dropoff  { left: 607px; top: 76px;  width: 401px; height: 847px; }

  .brand {
    position: absolute; left: 0; right: 0;
    color: var(--brand-orange);
    font-weight: 700; font-size: 28px; line-height: 27px;
    letter-spacing: 0.5px; text-transform: uppercase;
  }
  .tagline {
    position: absolute; left: 0; right: 0;
    color: var(--brand-orange);
    font-weight: 400; font-size: 12px;
  }
  .contact {
    position: absolute; left: 0; right: 0;
    display: flex; flex-direction: column; align-items: center;
  }
  .contact__name {
    color: var(--name-cyan);
    font-weight: 400; font-size: 30px; line-height: 32px;
    padding: 0 2px 2px;
    border-bottom: 1px solid var(--rule-orange);
  }
  .contact__rule {
    width: 180px; height: 1px; margin-top: 3px;
    background: var(--rule-soft);
  }
  .contact__line {
    color: var(--name-cyan);
    font-weight: 300; font-size: 10px; line-height: 15px;
  }

  .card--business .brand   { top: 9px; }
  .card--business .tagline { top: 83px; }
  .card--business .contact { top: 116px; }

  .card--dropoff .brand   { top: 6px; }
  .card--dropoff .tagline { top: 70px; }
  .card--dropoff .contact { top: 761px; }
</style>
</head>
<body>
<main class="canvas">
  <section class="card card--business" aria-label="Business card">
    <h1 class="brand">Tidecrest<br>Audio</h1>
    <p class="tagline">Clear sound for every stage ... felt deep</p>
    <div class="contact">
      <p class="contact__name">Doran Pelley</p>
      <span class="contact__rule"></span>
      <p class="contact__line">doran@tidecrestaudio.example.com.au</p>
      <p class="contact__line">0482 356 071</p>
    </div>
  </section>

  <section class="card card--dropoff" aria-label="Drop-off card">
    <h2 class="brand">Tidecrest<br>Audio</h2>
    <p class="tagline">Clear sound for every stage ... felt deep</p>
    <div class="contact">
      <p class="contact__name">Doran Pelley</p>
      <span class="contact__rule"></span>
      <p class="contact__line">doran@tidecrestaudio.example.com.au</p>
      <p class="contact__line">0482 356 071</p>
    </div>
  </section>
</main>
</body>
</html>
```